I am writing a book called "JOY FINDS THE WAY "

I NEED A BOOK COVER FOR MY BOOK" JOY FINDS THE WAY"
so what was the question? " ( this in smaller font)

"Joy Finds the Way " will need to designed to eventually be a logo , banner and business card
COLOURS MAINLY ORANGE AND WHITE (with accents bright colour )

THE BOOK IS MY LAUGHTER JOURNEY AS A PERFORMER AND ADVENTURE INDIA LEARNING ABOUT LAUGHTER YOGA WHICH I WILL BE TEACHING

I do not want photos on the front cover ..
The look could be modern and eye-catching
I have also just been to India to learn Laughing Yoga with Dr Rohit Venkatesh

Thank-you so much everyone for your brilliant designs . i am overwhelmed with your talent . i hope to work with you all again soon ! Moira  

Target Market(s)

"Adults based in western speaking countries aged 25 to 60 that want to learn to laugh more
Also this book will be sold at my conference workshops

Industry/Entity Type

Business

Requirements
Must have
• ORANGE AND WHITE
CAN HAVE AQUA , HOT PINK , LIME GREEN, YELLOW ACCENTS

THESE WILL BE DIFFERENT AREAS WILL COVERING IN MY BOOK
EG LAUGHTER NAD BREAT CANCER ( PINK)
LAUGHTER NAD DEPRESSION ( BLUE)
LAUGHTER AND KIDS ( YELLOW)

NO Photos on front cover
Should not have
• No photos

```html
<!DOCTYPE html>
<html lang="en">
<head>
<meta charset="utf-8">
<title>Joy Finds the Way – Book Cover</title>
<link rel="stylesheet" href="https://fonts.googleapis.com/css2?family=Fredoka:wght@600;700&family=Lobster&family=Open+Sans:wght@700&display=swap">
<style>
  :root {
    --bg: #ededed;
    --paper: #f7f7f7;
    --orange: #e2521a;
    --orange-deep: #c8410f;
    --title-fill: #fbe3c8;
    --title-edge: #d9621f;
    --ink: #1e1e1e;
    --white: #ffffff;
  }
  * { box-sizing: border-box; margin: 0; padding: 0; }
  html, body { width: 1200px; height: 800px; overflow: hidden; }
  body {
    background: var(--bg);
    display: flex;
    align-items: center;
    justify-content: center;
  }
  .cover-spread {
    display: flex;
    height: 610px;
    box-shadow: 0 10px 30px rgba(0,0,0,0.12);
  }
  .title {
    font-family: "Fredoka", sans-serif;
    font-weight: 700;
    color: var(--title-fill);
    text-align: center;
    text-transform: uppercase;
    line-height: 1.08;
    letter-spacing: 0.5px;
    -webkit-text-stroke: 3px var(--title-edge);
    paint-order: stroke fill;
    text-shadow: 0 0 6px rgba(226,82,26,0.55), 0 2px 3px rgba(200,65,15,0.35);
  }
  .author-script {
    font-family: "Lobster", cursive;
  }

  /* Back cover */
  .back-cover {
    width: 390px;
    background: var(--paper);
    position: relative;
    padding: 22px 38px 0;
  }
  .back-cover .author-script {
    color: var(--orange);
    font-size: 14px;
    text-align: center;
    margin-left: 90px;
  }
  .back-cover .title {
    font-size: 42px;
    margin-top: 2px;
  }
  .blurb {
    font-family: "Open Sans", sans-serif;
    font-weight: 700;
    font-size: 9.6px;
    line-height: 1.38;
    color: var(--ink);
    text-align: justify;
    text-align-last: center;
    margin-top: 14px;
  }
  .back-footer {
    position: absolute;
    left: 38px;
    right: 20px;
    bottom: 30px;
    display: flex;
    justify-content: space-between;
  }
  .back-footer .slot {
    width: 112px;
    height: 40px;
    background: var(--orange);
    color: var(--white);
    font-family: "Open Sans", sans-serif;
    font-size: 8px;
    display: flex;
    align-items: center;
    justify-content: center;
  }

  /* Spine */
  .spine {
    width: 30px;
    background: var(--paper);
    border-left: 1px solid #dcdcdc;
    border-right: 1px solid #dcdcdc;
    display: flex;
    flex-direction: column;
    align-items: center;
    padding: 18px 0 14px;
  }
  .spine .title {
    writing-mode: vertical-rl;
    font-size: 24px;
    -webkit-text-stroke: 2px var(--title-edge);
    white-space: nowrap;
  }
  .spine .author-script {
    writing-mode: vertical-rl;
    color: var(--orange);
    font-size: 11px;
    margin-top: auto;
  }

  /* Front cover */
  .front-cover {
    width: 390px;
    background: var(--paper);
    position: relative;
    display: flex;
    flex-direction: column;
    align-items: center;
    justify-content: center;
    padding-bottom: 34px;
  }
  .front-cover .title {
    font-size: 56px;
  }
  .subtitle {
    font-family: "Lobster", cursive;
    color: var(--orange);
    font-size: 24px;
    margin-top: 22px;
    text-align: center;
  }
  .author-band {
    position: absolute;
    left: 0;
    right: 0;
    bottom: 0;
    height: 34px;
    background: var(--orange);
    display: flex;
    align-items: center;
    justify-content: center;
    color: var(--white);
    font-size: 18px;
  }
</style>
</head>
<body>
  <div class="cover-spread">
    <section class="back-cover">
      <p class="author-script">Author Name</p>
      <h2 class="title">Joy Finds<br>the Way</h2>
      <p class="blurb">Lorem ipsum dolor sit amet, consectetur adipisicing elit, sed do eiusmod tempor incididunt ut labore et dolore magna aliqua. Ut enim ad minim veniam, quis nostrud exercitation. Lorem ipsum dolor sit amet, consectetur adipisicing elit, sed do eiusmod tempor incididunt ut labore et dolore magna aliqua. Ut enim ad minim veniam, quis nostrud exercitation. Lorem ipsum dolor sit amet, consectetur adipisicing elit, sed do eiusmod tempor incididunt ut labore et dolore magna aliqua. Ut enim ad minim veniam, quis nostrud exercitation. Lorem ipsum dolor sit amet, consectetur adipisicing elit, sed do eiusmod tempor incididunt ut labore et dolore magna aliqua. Ut enim ad minim veniam, quis nostrud exercitation. Lorem ipsum dolor sit amet, consectetur adipisicing elit, sed do eiusmod tempor incididunt ut labore et dolore magna aliqua. Ut enim ad minim veniam, quis nostrud exercitation. Lorem ipsum dolor sit amet, consectetur adipisicing elit, sed do eiusmod tempor incididunt ut labore et dolore magna aliqua. Ut enim ad minim veniam, quis nostrud exercitation. Lorem ipsum dolor sit amet, consectetur adipisicing elit, sed do eiusmod tempor incididunt ut labore et dolore magna aliqua. Ut enim ad minim veniam, quis nostrud exercitation. Lorem ipsum dolor sit amet, consectetur adipisicing elit, sed do eiusmod tempor incididunt ut labore et dolore magna aliqua. Ut enim ad minim veniam, quis nostrud exercitation. Lorem ipsum dolor sit amet, consectetur adipisicing elit, sed do eiusmod tempor incididunt ut labore et dolore magna aliqua. Ut enim ad minim veniam, quis nostrud exercitation.</p>
      <div class="back-footer">
        <div class="slot">LOGO</div>
        <div class="slot">ISBN</div>
      </div>
    </section>

    <aside class="spine">
      <span class="title">Joy Finds the Way</span>
      <span class="author-script">Author Name</span>
    </aside>

    <section class="front-cover">
      <h1 class="title">Joy Finds<br>the Way</h1>
      <p class="subtitle">so what was the question?</p>
      <div class="author-band author-script">Author Name</div>
    </section>
  </div>
</body>
</html>
```